KelVor Neutraceuticals Needs a New Label Design!

Kelvor is a neutraceutical line of vitamins, supplements and protein powders. We are looking for a new look/feel for our labels to really make them pop off the shelf.

Some brands we like are:
www.brimu.example
www.velopraxa.example
www.quendil.example

We are going to have square bottles and caps that will most likely be white or clear. We'd like a look/feel that uses bold colors and perhaps foil to make the design stand out.

The labels may be different colors for each product, but the general look/feel should be the same. To learn more about KelVor, take a look at www.tq-pharmlabs.example/kelvor.

We are also reformulating to make our products natural, organic and non-GMO. A look gearing more towards a holistic feel might work!

We have a logo that we cannot change, but we are not committed to the colors of it (Orange and green) and it does NOT have to be prominent on the label itself.

Design must utilize our icons (see website and attached files)

Kelvors tagline is: Shaping Sturdy Lives

Reason: We wanted to extend this project to give designers a bit more time to work on it!

Target Market(s)

Women and Men who are serious about their health, women purchasing vitamins for family....

Industry/Entity Type

Health And Wellness

Font styles to use
Decorative

Requirements
Must have
• Must:
• -Utilize our icons
• -Have bold colors
• -Stand out on a shelf
Nice to have
• The "Vor" in "KelVor" should stand out

```html
<!DOCTYPE html>
<html lang="en">
<head>
<meta charset="utf-8">
<title>Kelvor Super B Complex Label</title>
<link href="https://fonts.googleapis.com/css2?family=Open+Sans:wght@300;400;700&family=Roboto+Condensed:ital,wght@0,400;1,300&family=Montserrat:wght@400;700&family=Archivo+Black&family=Arimo:wght@400;700&display=swap" rel="stylesheet">
<style>
  :root {
    --page: #e6e6e6;
    --label: #f3f3f3;
    --panel: #fbfbfb;
    --green: #3aad3a;
    --green-dark: #23902b;
    --lime: #cfe23a;
    --orange: #ef6a1f;
    --orange-deep: #e55a16;
    --ink: #1c1c1c;
    --grey-text: #4a4a4a;
    --icon-red: #e0202a;
    --icon-blue: #3fb4e6;
    --icon-tan: #b39a5c;
    --icon-yellow: #f2b51c;
    --icon-purple: #6a3596;
    --icon-teal: #32b3a7;
  }
  * { box-sizing: border-box; margin: 0; padding: 0; }
  html, body { width: 1200px; height: 1200px; overflow: hidden; background: var(--page); }
  .label {
    position: absolute; left: 20px; top: 404px; width: 1160px; height: 392px;
    background: var(--label); overflow: hidden;
    box-shadow: 0 2px 10px rgba(0,0,0,.18);
  }
  .label-swoosh { position: absolute; inset: 0; }
  .panel {
    position: absolute; top: 29px; height: 324px; width: 330px;
    background: var(--panel); border: 1px solid #d4d4d4;
    box-shadow: 0 1px 4px rgba(0,0,0,.12);
  }
  .panel-directions {
    left: 38px; padding: 12px 8px 8px 8px;
    font-family: "Montserrat", sans-serif; font-size: 8.6px; line-height: 9.6px;
    color: var(--grey-text); text-align: justify;
  }
  .panel-directions p { margin-bottom: 9px; }
  .panel-directions strong { color: var(--ink); font-weight: 700; letter-spacing: .6px; }
  .panel-directions .warning { font-weight: 700; color: var(--ink); letter-spacing: .6px; text-transform: uppercase; }
  .panel-facts { left: 798px; padding: 7px; }
  .facts-box { border: 1.5px solid var(--ink); height: 100%; padding: 4px 6px; font-family: "Arimo", sans-serif; color: var(--ink); }
  .facts-title { font-family: "Archivo Black", sans-serif; font-size: 25px; line-height: 28px; letter-spacing: .2px; }
  .facts-serving { font-size: 8px; border-bottom: 6px solid var(--ink); padding-bottom: 2px; }
  .facts-table { width: 100%; border-collapse: collapse; font-size: 8px; }
  .facts-table th { font-size: 6px; font-weight: 700; text-align: center; padding: 2px 0; border-bottom: 3px solid var(--ink); line-height: 7px; }
  .facts-table td { padding: 1.5px 0; border-bottom: 1px solid var(--ink); line-height: 10px; vertical-align: top; }
  .facts-table td.amt { width: 58px; }
  .facts-table td.dv { width: 30px; text-align: right; }
  .facts-table .indent { padding-left: 12px; }
  .facts-table tr:last-child td { border-bottom: 5px solid var(--ink); }
  .facts-other { font-size: 7.6px; line-height: 9px; margin-top: 4px; }
  .facts-other b { font-weight: 700; }
  .count {
    position: absolute; top: 21px; font-family: "Roboto Condensed", sans-serif;
    text-align: left; line-height: 1;
  }
  .count-number { font-size: 28px; color: var(--orange); letter-spacing: -1px; }
  .count-unit { font-size: 8px; color: var(--grey-text); display: block; }
  .count-unit.small { font-size: 5px; }
  .count-capsules { left: 437px; }
  .count-days { left: 700px; }
  .count-days .count-unit { font-size: 11px; }
  .count-days .count-unit.small { font-size: 8px; }
  .brand {
    position: absolute; left: 441px; width: 288px; top: 40px; text-align: center;
  }
  .brand-dot { display: block; width: 46px; height: 46px; border-radius: 50%; background: var(--orange); margin: 0 auto 6px; }
  .brand-name { font-family: "Open Sans", sans-serif; font-weight: 300; font-size: 50px; line-height: 52px; color: var(--ink); }
  .product-name {
    position: absolute; left: 421px; width: 328px; top: 150px; text-align: center;
    font-family: "Open Sans", sans-serif; font-weight: 400; font-size: 66px; line-height: 66px;
    color: var(--green); letter-spacing: -2px;
  }
  .product-bar {
    position: absolute; left: 441px; top: 219px; width: 288px; height: 25px;
    background: linear-gradient(var(--orange), var(--orange-deep));
    color: #fff; text-align: center;
    font-family: "Open Sans", sans-serif; font-weight: 700; font-size: 24px; line-height: 25px; letter-spacing: 2px;
  }
  .tagline {
    position: absolute; left: 441px; width: 288px; top: 255px; text-align: center;
    font-family: "Roboto Condensed", sans-serif; font-style: italic; font-weight: 300;
    font-size: 17px; line-height: 17px; color: var(--grey-text);
  }
  .category {
    position: absolute; left: 441px; width: 288px; top: 298px; text-align: center;
    font-family: "Montserrat", sans-serif; font-weight: 700; font-size: 13.5px; color: #3a3a3a; letter-spacing: .3px;
  }
  .icon-row { position: absolute; left: 440px; top: 351px; display: flex; gap: 8px; }
  .icon-tile { width: 44px; height: 26px; border: 2px solid #fff; box-shadow: 0 0 0 1px rgba(0,0,0,.15); }
  .icon-tile.red { background: var(--icon-red); }
  .icon-tile.blue { background: var(--icon-blue); }
  .icon-tile.tan { background: var(--icon-tan); }
  .icon-tile.yellow { background: var(--icon-yellow); }
  .icon-tile.purple { background: var(--icon-purple); }
  .icon-tile.teal { background: var(--icon-teal); }
</style>
</head>
<body>
<main class="label">
  <svg class="label-swoosh" width="1160" height="392" viewBox="0 0 1160 392" aria-hidden="true">
    <defs>
      <linearGradient id="swooshGreen" x1="0" y1="0" x2="1" y2="0">
        <stop offset="0" stop-color="#2f9e33"/>
        <stop offset=".5" stop-color="#57b83a"/>
        <stop offset="1" stop-color="#2f9e33"/>
      </linearGradient>
    </defs>
    <path d="M0 300 C 300 340, 700 300, 1160 250 L1160 392 L0 392 Z" fill="#d9d9d9"/>
    <path d="M0 318 C 300 350, 700 310, 1160 262 L1160 392 L0 392 Z" fill="var(--lime)"/>
    <path d="M0 328 C 320 356, 700 322, 1160 278 L1160 392 L0 392 Z" fill="url(#swooshGreen)"/>
    <path d="M0 345 C 320 372, 720 338, 1160 300" stroke="#e8ef6a" stroke-width="3" fill="none" opacity=".8"/>
    <path d="M0 360 C 340 384, 740 352, 1160 320 L1160 392 L0 392 Z" fill="var(--green-dark)" opacity=".55"/>
  </svg>

  <section class="panel panel-directions">
    <p><strong>SUGGESTED USE:</strong> Two capsules taken daily with meals as a diteary supplement, or as directed by a health care professional.</p>
    <p><strong>CAUTION:</strong> Do not exceed recommended dose. This Product is not intended for pregnant or nursing mothers, children under the age of 18, or persons with a known medical condition including any cardiovascular disorder and hypotension (low blood pressure). If you have questions about the advisability of taking this product, consult your physician prior to use. This product is manufacured and packaged in a facility which may also process milk, soy, wheat, egg peanuts,tree nuts and shelfish. This product is manufacured and packaged in a facility which may also process milk, soy, wheat, egg peanuts,tree nuts and shelfish.</p>
    <p class="warning">Keep out of reach of children, do not use if safety seal is damaged or missing. Store in a cool, dry place.</p>
    <p>These statements have not been evaluated by the Food and Drug Administration. This product is not intended to treat, cure, prevent or diagnose any disease.</p>
  </section>

  <div class="count count-capsules"><span class="count-number">180</span><span class="count-unit">CAPSULES</span><span class="count-unit small">SUPPLEMENT</span></div>
  <div class="count count-days"><span class="count-number">30</span><span class="count-unit">DAY</span><span class="count-unit small">SUPPLY</span></div>

  <div class="brand"><span class="brand-dot"></span><span class="brand-name">Kelvor</span></div>
  <h1 class="product-name">SUPER B</h1>
  <div class="product-bar">COMPLEX</div>
  <p class="tagline">The Super hero of all vitamins<br>Super B to the rescue</p>
  <p class="category">DIETARY SUPPLRMENT</p>

  <div class="icon-row">
    <div class="icon-tile red" role="img" aria-label="Heart health icon"></div>
    <div class="icon-tile blue" role="img" aria-label="Brain health icon"></div>
    <div class="icon-tile tan" role="img" aria-label="Joint health icon"></div>
    <div class="icon-tile yellow" role="img" aria-label="Eye health icon"></div>
    <div class="icon-tile purple" role="img" aria-label="Digestive health icon"></div>
    <div class="icon-tile teal" role="img" aria-label="Liver health icon"></div>
  </div>

  <section class="panel panel-facts">
    <div class="facts-box">
      <div class="facts-title">Supplement Facts</div>
      <div class="facts-serving">Serving Size 1 Tablet</div>
      <table class="facts-table">
        <tr><th></th><th>Amount Per<br>Serving</th><th style="text-align:right">% Daily<br>Value</th></tr>
        <tr><td>Vitamin A (as retinyl acetate and<br><span class="indent">50% as beta-carotene)</span></td><td class="amt">5000 IU</td><td class="dv">100%</td></tr>
        <tr><td>Vitamin C (as ascorbic acid)</td><td class="amt">60 mg</td><td class="dv">100%</td></tr>
        <tr><td>Vitamin D (as cholecalciferol)</td><td class="amt">400 IU</td><td class="dv">100%</td></tr>
        <tr><td>Vitamin E (as dl-alpha tocopheryl acetate)</td><td class="amt">30 IU</td><td class="dv">100%</td></tr>
        <tr><td>Thiamin (as thiamin mononitrate)</td><td class="amt">1.5 mg</td><td class="dv">100%</td></tr>
        <tr><td>Riboflavin</td><td class="amt">1.7 mg</td><td class="dv">100%</td></tr>
        <tr><td>Niacin (as niacinamide)</td><td class="amt">20 mg</td><td class="dv">100%</td></tr>
        <tr><td>Vitamin B<sub>6</sub> (as pyridoxine hydrochloride)</td><td class="amt">2.0 mg</td><td class="dv">100%</td></tr>
        <tr><td>Folate (as folic acid)</td><td class="amt">400 mcg</td><td class="dv">100%</td></tr>
        <tr><td>Vitamin B<sub>12</sub> (as cyanocobalamin)</td><td class="amt">6 mcg</td><td class="dv">100%</td></tr>
        <tr><td>Biotin</td><td class="amt">30 mcg</td><td class="dv">10%</td></tr>
        <tr><td>Pantothenic Acid (as calcium pantothenate)</td><td class="amt">10 mg</td><td class="dv">100%</td></tr>
      </table>
      <p class="facts-other"><b>Other ingredients:</b> Gelatin, lactose, magnesium stearate, microcrystalline cellulose, FD&amp;C Yellow No. 6, propylene glycol, propylparaben, and sodium benzoate.</p>
    </div>
  </section>
</main>
</body>
</html>
```